Website Revamp to a Legal Tech Company

We are a Legal Technology Company and we are revamping our whole company from the logo (already done) to the website. We have built a custom portal and harnessed the use of AI and automation.

Current Website - https://www.verantiq.com/

We need a new website that looks like a tech company
Some examples of websites for samples
1. What we have today - https://www.verantiq.com/
2. https://plumbrivet.com/
3. https://www.mossferns.com/
4. https://www.tavu.com/
5.https://www.brightkolaw.com/
6. https://www.sudorapt.com/

Hope this helps. Let's start with the Home page.
Once we agree on the basis design and the first 3-4 pages - we can handle the coding etc. Will have the content over once we have the basic homepage design.

Links that we will possibly have and want
1. Home
2. About Us
3. Place your Order
4. Free First File offer to all new customers
5. Services/Products
6. Transparent Pricing
7. Contact Us

Terms & Conditions and Privacy Policy will be added at the bottom of the page but our internal designers.

Hope this helps.

Target Market(s)

Personal Injury Law Firms in the US

Industry/Entity Type

Legal Tech Services

Coding

Coded - Design and coding required

Number of Pages Required

4 page

Colors

Designer to choose colors to be used in the design.

Requirements
Must have
• Need to look like a Tech company website
Nice to have
• The color Blue

```html
<!DOCTYPE html>
<html lang="en">
<head>
<meta charset="utf-8">
<title>Verantiq — Experience Offshore Advantage</title>
<link href="https://fonts.googleapis.com/css2?family=Jost:wght@400;500;600;700&display=swap" rel="stylesheet">
<style>
:root{
  --blue:#1f6fe5;
  --navy:#0f5499;
  --ink:#121826;
  --muted:#4a5160;
  --pale:#eef4fd;
  --field:#f0f1f3;
  --white:#ffffff;
  --star:#f5a623;
}
*{box-sizing:border-box;margin:0;padding:0}
html,body{width:1200px;height:3927px;overflow:hidden}
body{position:relative;font-family:'Jost',sans-serif;color:var(--ink);background:var(--white)}
.abs{position:absolute}
a{color:inherit}
.btn{position:absolute;display:flex;align-items:center;justify-content:center;border-radius:22px;background:var(--blue);color:var(--white);font-weight:500;font-size:14px;height:38px;text-decoration:none}
.accent{color:var(--blue)}

.topbar{left:0;top:0;width:1200px;height:42px;background:var(--navy);color:var(--white);font-size:13px;display:flex;align-items:center;justify-content:center;text-decoration:underline}
.hero-bg{left:0;top:42px;width:1200px;height:520px;background:linear-gradient(110deg,#f4f8fe 0%,#ffffff 55%,#f1f6fe 100%)}
.logo{display:flex;align-items:center;gap:10px}
.logo-mark{width:26px;height:26px;border-radius:6px;background:var(--navy)}
.logo-name{font-weight:600;font-size:24px;color:var(--navy)}
.nav{left:428px;top:76px;display:flex;gap:25px;font-size:13px;font-weight:500}
.nav-cta{left:950px;top:65px;width:109px;height:40px;font-size:14px}

.hero-title{left:126px;top:193px;font-size:48px;font-weight:600;line-height:68px}
.hero-title .underline{border-bottom:3px solid var(--navy);padding-bottom:2px}
.hero-text{left:126px;top:349px;width:410px;font-size:15px;line-height:25px}
.play{left:263px;top:423px;display:flex;align-items:center;gap:12px;font-weight:600;font-size:14px}
.play-dot{width:38px;height:38px;border-radius:50%;background:var(--blue);display:flex;align-items:center;justify-content:center}

.ring{border-radius:50%}
.review{left:1012px;top:178px;width:136px;height:102px;background:var(--white);border-radius:10px;box-shadow:0 6px 20px rgba(20,60,130,.12);padding:12px}
.review .score{font-size:22px;font-weight:500;color:var(--navy);margin-top:6px}
.review small{font-size:9px}
.happy{left:604px;top:445px;width:247px;height:78px;background:var(--white);border-radius:10px;box-shadow:0 6px 20px rgba(20,60,130,.12);display:flex;align-items:center;padding:0 22px;font-size:13px;font-weight:500;line-height:17px;gap:28px}
.avatars{display:flex}
.avatars span{width:34px;height:34px;border-radius:50%;border:2px solid #fff;margin-left:-10px}

.svc{top:598px;width:444px;height:131px;background:var(--blue);border-radius:8px;color:var(--white);display:flex;gap:24px;padding:24px}
.svc-icon{width:70px;height:70px;border-radius:8px;background:var(--white);flex:none;display:flex;align-items:center;justify-content:center}
.svc h3{font-size:15px;font-weight:500;line-height:25px;margin-top:2px}
.svc .more{font-size:12px;font-weight:600;text-decoration:underline;margin-top:8px;display:block}

.photo{border-radius:8px}
.sec-title{font-size:28px;font-weight:600}
.body-text{font-size:12.5px;line-height:22.5px;color:var(--muted)}
.body-text + .body-text{margin-top:14px}

.cases{left:0;top:1269px;width:1200px;height:628px;background:var(--navy);color:var(--white)}
.tabs{position:absolute;left:0;width:1200px;top:1382px;display:flex;justify-content:center;gap:14px}
.tab{height:38px;border:1.5px solid var(--white);border-radius:20px;padding:0 18px;font-size:13px;font-weight:500;display:flex;align-items:center;color:var(--white)}
.tab.active{background:var(--white);color:var(--navy)}
.case-text p{font-size:12px;line-height:22.5px;color:#e8eef8}
.case-text p + p{margin-top:14px}

.why-card{top:2059px;width:212px;height:270px;border-radius:14px;background:var(--pale);padding:26px 28px}
.why-card.raised{background:var(--white);box-shadow:0 8px 28px rgba(20,60,130,.12)}
.why-icon{width:56px;height:56px;border-radius:10px;background:var(--blue);display:flex;align-items:center;justify-content:center}
.why-card h3{font-size:17px;font-weight:500;margin-top:16px;line-height:22px}
.why-card p{font-size:12px;line-height:22.5px;color:var(--muted);margin-top:12px}

.post{top:2567px;width:291px}
.post .img{height:179px;border-radius:4px}
.post h3{font-size:15px;font-weight:500;line-height:24px;margin-top:20px}
.post p{font-size:11.5px;line-height:20px;color:var(--muted);margin-top:5px}
.post .more{font-size:12px;font-weight:500;color:var(--blue);text-decoration:underline;display:block;margin-top:10px}

.reach{left:142px;top:2980px;width:393px;height:518px;background:var(--blue);border-radius:16px;color:var(--white);padding:30px 31px}
.reach h3{font-size:21px;font-weight:500}
.reach p{font-size:12px;line-height:22px;margin-top:12px}
.reach h4{font-size:15px;font-weight:500;margin-top:22px}
.reach .row{display:flex;gap:12px;font-size:12px;line-height:16px;margin-top:12px;align-items:flex-start}
.reach .row svg{flex:none}

.field{left:610px;width:447px;height:43px;background:var(--field);border:1px solid #e4e6ea;border-radius:4px;font-size:12px;color:#555;padding:13px 14px}

.footer{left:0;top:3584px;width:1200px;height:343px;background:var(--navy);color:var(--white)}
.fcol h4{font-size:15px;font-weight:500;margin-bottom:12px}
.fcol li{list-style:none;font-size:12px;line-height:28px}
.social{width:30px;height:30px;border-radius:50%;background:var(--white)}
</style>
</head>
<body>

<div class="abs topbar">Free First File Offer To All New Customers</div>
<div class="abs hero-bg"></div>

<header>
  <div class="abs logo" style="left:150px;top:70px">
    <span class="logo-mark"></span><span class="logo-name">Verantiq</span>
  </div>
  <nav class="abs nav">
    <a>Home</a><a>About Us</a><a>Place Your Order</a><a>Services/Products</a><a>Transparent Pricing</a>
  </nav>
  <a class="btn nav-cta">Contact Us</a>
</header>

<span class="abs ring" style="left:131px;top:125px;width:11px;height:11px;background:#9dbff2"></span>
<span class="abs ring" style="left:57px;top:246px;width:24px;height:24px;background:#8db4f0"></span>
<span class="abs ring" style="left:563px;top:343px;width:24px;height:24px;background:#b6cff5"></span>
<svg class="abs" style="left:368px;top:160px" width="24" height="20"><path d="M12 0 24 20H0z" fill="var(--blue)"/></svg>
<svg class="abs" style="left:6px;top:352px" width="36" height="76">
  <g fill="#f5a623"><circle cx="3" cy="3" r="1.6"/><circle cx="18" cy="3" r="1.6"/><circle cx="33" cy="3" r="1.6"/><circle cx="3" cy="27" r="1.6"/><circle cx="18" cy="27" r="1.6"/><circle cx="33" cy="27" r="1.6"/><circle cx="3" cy="51" r="1.6"/><circle cx="18" cy="51" r="1.6"/><circle cx="33" cy="51" r="1.6"/><circle cx="3" cy="73" r="1.6"/><circle cx="18" cy="73" r="1.6"/></g>
</svg>

<h1 class="abs hero-title">Experience <span class="underline">Offshore</span><br><span class="accent">Advantage</span></h1>
<p class="abs hero-text">Skilled medical experts. Substantial cost reduction. Quick turnaround. High Accuracy.</p>
<a class="btn" style="left:126px;top:423px;width:117px">Learn More</a>
<div class="abs play">
  <span class="play-dot"><svg width="14" height="14"><path d="M3 1 13 7 3 13z" fill="#fff"/></svg></span>
  Watch Our Video
</div>

<span class="abs ring" style="left:720px;top:160px;width:343px;height:343px;border:3px solid var(--blue)"></span>
<span class="abs ring" style="left:740px;top:180px;width:303px;height:303px;background:#cfe0fb"></span>
<div class="abs ring" role="img" aria-label="Business people shaking hands across an office table" style="left:757px;top:197px;width:269px;height:269px;background:linear-gradient(150deg,#e9edf2,#9aa6b6 60%,#4d5868)"></div>

<div class="abs review">
  <div style="display:flex;align-items:center;gap:8px">
    <span class="ring" style="width:26px;height:26px;background:var(--blue);display:block"></span>
    <span style="color:var(--star);font-size:13px;letter-spacing:1px">★★★★★</span>
  </div>
  <div class="score">4.9/5.0</div>
  <small>Based on verified reviews</small>
</div>

<div class="abs happy">
  <span>Our Happy<br>Customers</span>
  <div class="avatars">
    <span style="background:#e7a03a" role="img" aria-label="Customer portrait"></span>
    <span style="background:#c8473c" role="img" aria-label="Customer portrait"></span>
    <span style="background:#8d4a3a" role="img" aria-label="Customer portrait"></span>
    <span style="background:var(--blue);color:#fff;display:flex;align-items:center;justify-content:center;font-size:18px">+</span>
  </div>
</div>

<div class="abs svc" style="left:142px">
  <div class="svc-icon"><svg width="38" height="40" fill="none" stroke="var(--blue)" stroke-width="2"><circle cx="19" cy="10" r="7"/><path d="M5 38V28c0-6 6-9 14-9s14 3 14 9v10zM13 22v8M25 22v6a3 3 0 0 1-6 0"/></svg></div>
  <div><h3>Our Services Personal Injury Medical Records Summaries and Reports</h3><a class="more">Read More →</a></div>
</div>
<div class="abs svc" style="left:614px">
  <div class="svc-icon"><svg width="40" height="40" fill="none" stroke="var(--blue)" stroke-width="2"><circle cx="20" cy="8" r="5"/><path d="M12 20c0-4 4-6 8-6s8 2 8 6"/><circle cx="8" cy="26" r="4"/><circle cx="32" cy="26" r="4"/><path d="M1 38c0-4 3-6 7-6s7 2 7 6M25 38c0-4 3-6 7-6s7 2 7 6M16 32h8"/></svg></div>
  <div><h3>Retrieval, Assembly and Organization of Medical Records</h3><a class="more">Read More →</a></div>
</div>

<span class="abs ring" style="left:140px;top:812px;width:82px;height:82px;background:#cfdff9"></span>
<div class="abs photo" role="img" aria-label="Doctor in a mask consulting with a patient at a desk" style="left:180px;top:852px;width:335px;height:325px;background:linear-gradient(160deg,#e9eef3,#b7c3cf 55%,#7e8c9c);border-bottom:4px solid var(--blue)"></div>
<h2 class="abs sec-title" style="left:619px;top:851px;font-size:27px">Organized Medical <span class="accent">Files</span></h2>
<div class="abs" style="left:619px;top:908px;width:428px">
  <p class="body-text">Verantiq employs a team with expertise in retrieving, assembling, reviewing, and summarizing medical records and bills. We support law firms by handling all medical records-related tasks, thereby allowing attorneys to focus on other very important case-related matters, such as proving liability, causation, and damages.</p>
  <p class="body-text">Verantiq is equipped to immediately handle any size project for a small, mid-sized, or large law firm. Our team works within a secure facility and adheres to the highest level of security and confidentiality in order to safeguard your client's records and privacy.</p>
</div>
<a class="btn" style="left:619px;top:1147px;width:117px">Learn More</a>

<section class="abs cases"></section>
<h2 class="abs sec-title" style="left:0;top:1317px;width:1200px;text-align:center;color:#fff">Cases We Support</h2>
<div class="tabs"><span class="tab active">Personal Injury</span><span class="tab">Mass Tort</span><span class="tab">Medical Malpractice Cases</span></div>
<h3 class="abs" style="left:141px;top:1498px;font-size:22px;font-weight:500;color:#fff">Personal Injury</h3>
<div class="abs case-text" style="left:141px;top:1550px;width:545px">
  <p>With high volumes of medical records to be reviewed, lawyers handling personal injury cases need to clearly understand the nature of the injury and medical treatment, the extent of the harm and damages, and estimates of the future costs. The attorneys needs to invest a significant amount of time in retrieving and reviewing the records, drafting a case summaries, drafting demand letters, preparing for litigation, and more.</p>
  <p>Through a team of professionals, we retrieve the medical records, review the records, draft chronological summaries that provide an overview of the records, review the bills and provide the evidence that you need to support your claims for damages. With investments in processes and systems, we are able to provide your firm with high-quality medical records-related services, achieve cost efficiencies, and improve turn-around time.</p>
</div>
<a class="btn" style="left:141px;top:1812px;width:107px;background:#fff;color:var(--navy)">Read More</a>
<div class="abs photo" role="img" aria-label="Doctor bandaging a patient's injured leg" style="left:755px;top:1477px;width:303px;height:362px;background:linear-gradient(160deg,#eef2f6,#b3c0cd 55%,#6f7f92)"></div>

<h2 class="abs sec-title" style="left:0;top:1978px;width:1200px;text-align:center">Why <span class="accent">Verantiq</span></h2>
<div class="abs why-card" style="left:142px">
  <div class="why-icon"><svg width="26" height="30" fill="none" stroke="#fff" stroke-width="2"><rect x="2" y="5" width="22" height="24" rx="3"/><rect x="8" y="1" width="10" height="6" rx="1"/><path d="M13 12v10M8 17h10"/></svg></div>
  <h3>Medical Records Solutions</h3>
  <p>We provide medical records solutions to small, mid-sized, or large law firms.</p>
</div>
<div class="abs why-card raised" style="left:377px">
  <div class="why-icon"><svg width="32" height="26" fill="none" stroke="#fff" stroke-width="2"><circle cx="16" cy="7" r="4"/><circle cx="6" cy="10" r="3"/><circle cx="26" cy="10" r="3"/><path d="M8 24c0-5 4-8 8-8s8 3 8 8M1 22c0-4 2-6 5-6M31 22c0-4-2-6-5-6"/></svg></div>
  <h3>Highly Trained Staff</h3>
  <p>Our staff has expertise in and received training on retrieving, reviewing, and summarizing medical records.</p>
</div>
<div class="abs why-card" style="left:610px">
  <div class="why-icon"><svg width="30" height="30" fill="none" stroke="#fff" stroke-width="2"><circle cx="16" cy="9" r="7"/><path d="M13 9l2 2 4-4M2 22l6-4h8l-4 4h6l8-6M2 28l6-2h12"/></svg></div>
  <h3>Highest Quality</h3>
  <p>We provide the highest quality medical records support services that will save your firm money, time, and effort.</p>
</div>
<div class="abs why-card" style="left:845px">
  <div class="why-icon"><svg width="26" height="30" fill="none" stroke="#fff" stroke-width="2"><path d="M13 2 24 6v9c0 7-5 11-11 13C7 26 2 22 2 15V6z"/><path d="M8 15l4 4 6-7"/></svg></div>
  <h3>HIPAA And HITECH</h3>
  <p>We are HIPAA and HITECH compliant, and our staff follows strict rules-based security protocols.</p>
</div>
<a class="btn" style="left:546px;top:2373px;width:107px">Read More</a>

<h2 class="abs sec-title" style="left:0;top:2494px;width:1200px;text-align:center">Our <span class="accent">Blog</span></h2>
<article class="abs post" style="left:142px">
  <div class="img" role="img" aria-label="Judge's gavel beside a smartphone showing social apps" style="background:linear-gradient(135deg,#e6e0d8,#a07850 55%,#4a3424)"></div>
  <h3>Intentional Misuse of Social Media App May Lead to Developer Liability</h3>
  <p>Social media and messaging applications have changed the way people communicate...</p>
  <a class="more">Read More →</a>
</article>
<article class="abs post" style="left:454px">
  <div class="img" role="img" aria-label="Doctor working at a computer in a clinic" style="background:linear-gradient(135deg,#eef1f4,#b9c1ca 55%,#3c434d)"></div>
  <h3>EHR &amp; EMR – How to use them effectively in a Med Mal case</h3>
  <p>Electronic Health Records (EHR) and Electronic Medical Records (EMR) provide a wealth of...</p>
  <a class="more">Read More →</a>
</article>
<article class="abs post" style="left:767px">
  <div class="img" role="img" aria-label="Two doctors reviewing notes in a hospital hallway" style="background:linear-gradient(135deg,#f1f3f2,#c6ccd4 55%,#52617a)"></div>
  <h3>Is it time to remove the word “independent” from “IME”?</h3>
  <p>Plaintiff’s bar has generally recognized that IMEs may be many things, but “independent”...</p>
  <a class="more">Read More →</a>
</article>

<aside class="abs reach">
  <h3>Reach Us</h3>
  <p>Wish to learn more about how we can benefit your law firm, or have any questions?</p>
  <p style="margin-top:8px">Contact us at our offices below.</p>
  <h4>Business Inquiries</h4>
  <div class="row"><svg width="16" height="18" fill="none" stroke="#fff" stroke-width="1.8"><path d="M8 17s6-6 6-10A6 6 0 0 0 2 7c0 4 6 10 6 10z"/><circle cx="8" cy="7" r="2"/></svg><span>4810 Harbor Vista Blvd, Suite 7J,<br>Coral Bay, FL 33199</span></div>
  <div class="row"><svg width="16" height="12" fill="#fff"><path d="M0 0h16v12H0z"/><path d="M0 0l8 6 8-6" stroke="var(--blue)" stroke-width="1.5" fill="none"/></svg><span>info@verantiq.com</span></div>
  <div class="row"><svg width="15" height="15" fill="#fff"><path d="M3 0l3 4-2 2c1 2 3 4 5 5l2-2 4 3-2 3C6 15 0 9 0 3z"/></svg><span>(555) 248-7019</span></div>
  <h4>Records Processing</h4>
  <div class="row"><svg width="16" height="18" fill="none" stroke="#fff" stroke-width="1.8"><path d="M8 17s6-6 6-10A6 6 0 0 0 2 7c0 4 6 10 6 10z"/><circle cx="8" cy="7" r="2"/></svg><span>72 Birchfield Lane<br>Eastbrook, New York 11799</span></div>
  <div class="row"><svg width="16" height="12" fill="#fff"><path d="M0 0h16v12H0z"/><path d="M0 0l8 6 8-6" stroke="var(--blue)" stroke-width="1.5" fill="none"/></svg><span>records@verantiq.com</span></div>
  <div class="row"><svg width="15" height="15" fill="#fff"><path d="M3 0l3 4-2 2c1 2 3 4 5 5l2-2 4 3-2 3C6 15 0 9 0 3z"/></svg><span>(555) 248-7019</span></div>
  <div class="row"><svg width="15" height="15" fill="#fff"><path d="M3 0l3 4-2 2c1 2 3 4 5 5l2-2 4 3-2 3C6 15 0 9 0 3z"/></svg><span>(555) 362-9184</span></div>
</aside>

<h2 class="abs sec-title" style="left:608px;top:2993px">Leave A <span class="accent">Message</span></h2>
<div class="abs field" style="top:3056px">Name*</div>
<div class="abs field" style="top:3112px">Email*</div>
<div class="abs field" style="top:3169px">Phone*</div>
<div class="abs field" style="top:3225px">Organization*</div>
<div class="abs field" style="top:3282px;height:132px">Your Message*</div>
<a class="btn" style="left:610px;top:3440px;width:114px">Submit Now</a>

<footer class="abs footer"></footer>
<div class="abs logo" style="left:142px;top:3690px">
  <span class="logo-mark" style="background:#fff;width:34px;height:34px"></span><span class="logo-name" style="color:#fff;font-size:30px">Verantiq</span>
</div>
<div class="abs fcol" style="left:418px;top:3646px;color:#fff"><h4>Quick Links</h4><ul><li>Home</li><li>About Us</li><li>Place Your Order</li><li>Services/Products</li><li>Transparent Pricing</li></ul></div>
<div class="abs fcol" style="left:596px;top:3646px;color:#fff"><h4>Resources</h4><ul><li>Privacy Policy</li><li>Terms &amp; Conditions</li><li>Contact Us</li></ul></div>
<div class="abs fcol" style="left:773px;top:3646px;color:#fff"><h4>Newsletter</h4></div>
<div class="abs" style="left:773px;top:3680px;width:285px;height:42px;background:#fff;border-radius:6px;display:flex;align-items:center;justify-content:space-between;padding:0 6px 0 18px;font-size:12px;color:#667">
  Enter your email
  <span style="width:36px;height:30px;border-radius:5px;background:var(--navy);display:flex;align-items:center;justify-content:center"><svg width="14" height="14" fill="#fff"><path d="M14 0 0 6l5 2 2 6z"/></svg></span>
</div>
<div class="abs" style="left:142px;top:3869px;width:916px;height:1px;background:rgba(255,255,255,.3)"></div>
<div class="abs" style="left:142px;top:3890px;color:#fff;font-size:12px">© 2018-2024, Verantiq</div>
<div class="abs" style="left:908px;top:3883px;display:flex;gap:10px">
  <span class="social"></span><span class="social"></span><span class="social"></span><span class="social"></span>
</div>

</body>
</html>
```